KALO Wave Co.
KALO Wave Co. - Sports
Creative Brief
Sports
www.kalowave.example
Inspired by Neptune, Roman God of the Sea, KALO Wave Co was created to produce the most cutting-edge performance and high quality boards EVER made, period.
With that being said, not everyone is meant to ride a KALO.
KALO Wave Co is a small company created by a group of close friends that LOVE the ocean, especially surfing. Our passion is in our work, and it shows in our ideas.
We want to portray the lifestyle of a true surfer: strapping their board on top of their jalopy, setting out for the unexplored coastline, and finding THE spot of their own.
Likes: Background dark in color (Feel of sunset over ocean) soft white writing. Image of surfer popping off wake on board Image of surfers *male and female having a good time (smiling, etc.) Dislike: Cookie-cutter templates
Black
Sunset Orange
Soft White
top
http://www.brimtrek.example/shop/us/en/ (background image)
http://www.dashfen.example/#/women/americacanada/teamriders/r.surf|marla_quenby (feel)
http://www.glowtrove.example/images/Waterfront%20at%20Night.jpg (photo lighting)
Edgy Cool Sexy Energy Tabs across top to include: Products, Technology, About Us, What's New, Contact Us Need good balance. Similar point of view of Tidelark/Brackenfoam/Gumbaroo Possible quote in small font "Life's too short to be ordinary" Would like to add small social network icons on lower right.

```html
<!DOCTYPE html>
<html lang="en">
<head>
<meta charset="utf-8">
<title>KALO Wave Co.</title>
<link rel="stylesheet" href="https://fonts.googleapis.com/css2?family=Arimo:wght@400;700&family=Permanent+Marker&display=swap">
<style>
  :root {
    --black: #0a0a0a;
    --panel-edge: #3a3a3a;
    --box: #111111;
    --box-edge: #4a4a4a;
    --sunset: #e8941f;
    --soft-white: #f1eee8;
    --muted: #c9c6c0;
    --icon: #6e6e6e;
  }
  * { box-sizing: border-box; margin: 0; padding: 0; }
  html, body { width: 1200px; height: 1099px; overflow: hidden; }
  body {
    position: relative;
    font-family: "Arimo", Arial, sans-serif;
    color: var(--soft-white);
    background:
      radial-gradient(ellipse 700px 300px at 20% 8%, #5a5a5a 0%, rgba(40,40,40,0) 70%),
      radial-gradient(ellipse 600px 260px at 85% 6%, #4a4a4a 0%, rgba(40,40,40,0) 70%),
      linear-gradient(180deg, #2b2b2b 0%, #161616 50%, #0c0c0c 78%, #3a3a3a 92%, #1a1a1a 100%);
  }
  .backdrop-wave {
    position: absolute; left: 0; right: 0; bottom: 0; height: 220px;
    background: linear-gradient(180deg, rgba(10,10,10,0) 0%, #4b4b4b 45%, #2a2a2a 70%, #8a8a8a 88%, #3b3b3b 100%);
    opacity: .75;
  }
  .brand {
    position: absolute; left: 104px; top: 66px; z-index: 2;
    display: flex; align-items: center; gap: 18px;
  }
  .brand-name {
    font-weight: 700; font-size: 88px; letter-spacing: 2px; line-height: 1;
    color: var(--soft-white);
  }
  .brand-sub {
    position: absolute; left: 4px; top: 120px;
    font-weight: 700; font-size: 18px; letter-spacing: 1px; white-space: nowrap;
    color: var(--soft-white);
  }
  .brand-dot {
    width: 100px; height: 100px; border-radius: 50%;
    background: var(--sunset);
  }
  .main-nav {
    position: absolute; left: 75px; top: 143px; width: 1057px; height: 70px; z-index: 1;
    background: var(--black);
  }
  .main-nav ul {
    list-style: none; position: absolute; left: 431px; top: 0; height: 70px;
    display: flex; align-items: center; gap: 34px;
  }
  .main-nav a {
    position: relative; white-space: nowrap;
    color: var(--soft-white); text-decoration: none;
    font-weight: 700; font-size: 15px; text-transform: uppercase; letter-spacing: .3px;
  }
  .main-nav a.current::after {
    content: ""; position: absolute; left: 50%; bottom: -20px; margin-left: -8px;
    border: 8px solid transparent; border-top-color: var(--sunset); border-bottom: 0;
  }
  .content-panel {
    position: absolute; left: 75px; top: 224px; width: 1057px; height: 670px;
    background: linear-gradient(180deg, #2e2e2e, #1f1f1f);
    border: 1px solid var(--panel-edge); border-radius: 6px;
  }
  .hero-strip {
    position: absolute; left: 104px; top: 262px; width: 999px; height: 349px;
    display: flex;
  }
  .hero-strip .photo { flex: 1; }
  .photo-surfer-male { background: linear-gradient(180deg, #7fb7d6 0%, #c79a78 60%, #a56f4f 100%); }
  .photo-sunset-couple { background: linear-gradient(180deg, #d9a04a 0%, #b9772d 45%, #3a2412 100%); }
  .photo-wave-air { background: linear-gradient(180deg, #2f6fae 0%, #5c99cf 40%, #e8f1f6 70%, #2a6d9c 100%); }
  .photo-surfer-female { background: linear-gradient(180deg, #cdb48a 0%, #b99064 50%, #3c6f7e 100%); }
  .info-box {
    position: absolute; top: 632px; height: 238px;
    background: var(--box); border: 1px solid var(--box-edge); border-radius: 4px;
  }
  .info-box h2 {
    font-weight: 700; font-size: 29px; text-transform: uppercase; letter-spacing: .5px;
    padding: 14px 0 0 22px; white-space: nowrap;
  }
  .info-box h2::after {
    content: ""; display: block; margin: 12px 0 0 -22px; height: 1px; background: var(--box-edge);
  }
  .about-box { left: 98px; width: 486px; }
  .about-box p {
    font-size: 15px; line-height: 23px; color: var(--muted);
    padding: 0 22px; margin-top: 16px;
  }
  .about-box p + p { margin-top: 23px; }
  .products-box { left: 626px; width: 477px; }
  .carousel {
    position: absolute; left: 0; top: 60px; width: 100%; height: 90px;
  }
  .carousel .arrow { position: absolute; top: 37px; }
  .carousel .arrow.prev { left: 14px; }
  .carousel .arrow.next { right: 14px; }
  .thumbs { position: absolute; left: 45px; top: 0; display: flex; gap: 10px; }
  .thumb { width: 85px; height: 90px; border: 2px solid #ddd; }
  .thumb-1 { background: linear-gradient(180deg, #8aa6a0, #4d5f4a); }
  .thumb-2 { background: linear-gradient(180deg, #3d79ad, #d8e6ee); }
  .thumb-3 { background: linear-gradient(180deg, #b7a57c, #6b5a3d); }
  .thumb-4 { background: linear-gradient(180deg, #e7ecef, #5d86a8); }
  .products-box p {
    position: absolute; left: 22px; top: 165px;
    font-size: 15px; color: var(--muted);
  }
  .products-box .see-more {
    position: absolute; left: 22px; top: 198px;
    font-weight: 700; font-size: 15px; color: var(--soft-white); text-decoration: none;
  }
  .tagline {
    position: absolute; left: 100px; top: 932px; width: 740px; height: 44px;
    display: flex; align-items: center; white-space: nowrap; overflow: hidden;
    font-family: "Permanent Marker", "Arimo", cursive;
    font-size: 30px; letter-spacing: 1px; text-transform: uppercase;
    color: var(--soft-white);
  }
  .social-links {
    position: absolute; left: 868px; top: 932px;
    display: flex; gap: 14px; list-style: none;
  }
  .social-links li {
    width: 48px; height: 44px; border-radius: 6px; background: var(--icon);
  }
</style>
</head>
<body>
  <div class="backdrop-wave" role="img" aria-label="Dark ocean wave backdrop with grey spray"></div>

  <header>
    <div class="brand">
      <span class="brand-name">KALO</span>
      <span class="brand-dot"></span>
      <span class="brand-sub">Wave Co.</span>
    </div>
    <nav class="main-nav">
      <ul>
        <li><a href="#">Products</a></li>
        <li><a href="#">Technology</a></li>
        <li><a href="#" class="current">About Us</a></li>
        <li><a href="#">What's New</a></li>
        <li><a href="#">Contact Us</a></li>
      </ul>
    </nav>
  </header>

  <main>
    <div class="content-panel"></div>

    <section class="hero-strip">
      <div class="photo photo-surfer-male" role="img" aria-label="Smiling young male surfer holding his board"></div>
      <div class="photo photo-sunset-couple" role="img" aria-label="Silhouetted couple with surfboards at sunset"></div>
      <div class="photo photo-wave-air" role="img" aria-label="Surfer launching off a breaking wave"></div>
      <div class="photo photo-surfer-female" role="img" aria-label="Female surfer sitting on her board at the shore"></div>
    </section>

    <section class="info-box about-box">
      <h2>Who We Are</h2>
      <p>KALO Wave Co is a small company created by a group of close friends that LOVE the ocean, especially surfing. Our passion is in our work, and it shows in our ideas.</p>
      <p>Strap your board to your ride, set out for unexplored coastline, and find THE spot of your own.</p>
    </section>

    <section class="info-box products-box">
      <h2>Summer 2011 Products</h2>
      <div class="carousel">
        <svg class="arrow prev" width="10" height="14" viewBox="0 0 10 14"><path d="M9 0 L0 7 L9 14 Z" fill="#f1eee8"/></svg>
        <div class="thumbs">
          <div class="thumb thumb-1" role="img" aria-label="Surfboard product shot"></div>
          <div class="thumb thumb-2" role="img" aria-label="Surfer riding a wave"></div>
          <div class="thumb thumb-3" role="img" aria-label="Board and gear on the beach"></div>
          <div class="thumb thumb-4" role="img" aria-label="Surfer carving spray"></div>
        </div>
        <svg class="arrow next" width="10" height="14" viewBox="0 0 10 14"><path d="M1 0 L10 7 L1 14 Z" fill="#f1eee8"/></svg>
      </div>
      <p>Our passion is in our work, and it shows in our ideas.</p>
      <a class="see-more" href="#">SEE MORE</a>
    </section>
  </main>

  <footer>
    <p class="tagline">Life's too short to be ordinary</p>
    <ul class="social-links">
      <li aria-label="Social network link"></li>
      <li aria-label="Social network link"></li>
      <li aria-label="Social network link"></li>
      <li aria-label="Social network link"></li>
    </ul>
  </footer>
</body>
</html>
```